ZB - WESITE NEEDED PAGE: Clean / Modern / Pro & Dynamic

Zephyl-Brokers is a new insurance brokerage firm dealing exclusively with companies (BToB) providing the following property: Liabilities Insurance Insurances Automobile Insurance Insurances Construction% 26amp; Engineering Casualty Workmen 's Compensation Health Insurance Marime% 26amp; Transit Credit Insurance Young, Fast, Proactive and Dynamic we call ourselves Zephyl-Brokers because we are a "start-up" willing to make a difference in the market, bringing modernity and speed to our industry, still too bureaucratic / procedural / opaque uninitiated. We need something respecting the colors of our orange logtype; blue; white; black; easy to scroll, with simple information on the company; - who we are - our team (with the pictures) - what we do - what we do - contact us, contact us (google map) Luanda (Angola) Small company, just need something flashy / professional / structured / modern.

Target Market(s)

BtoB; Oil and gas companies; French speaking copying established in Angola, all industrials, factories and importers of goods.

Industry/Entity Type

Insurance Broker

Font styles to use
Sans Serif

Colors

Requirements
Must have
• We need something respecting the colors of our orange logtype; blue; white; black; easy to scroll, with simple information on the company; - who we are - our team (with the pictures) - what we do - what we do - contact us, contact us (google map) Luanda (Angola) Small company, just need something flashy / professional / structured / modern.
Nice to have
• A page format
Should not have
• WE DO NOT WANT A REFER TO OUR LOGO, but a Home Page for our Website with the basics categories ... >> PLEASE CAREFULLY USE THE RIGHT COLOR OF THE LOGOTYPE which are the ones enclosed Orange / Turquoise / Black as per the business card .

```html
<!DOCTYPE html>
<html lang="en">
<head>
<meta charset="utf-8">
<title>Zephyl-Brokers</title>
<link rel="stylesheet" href="https://fonts.googleapis.com/css2?family=Rubik:wght@400;500;700&family=Open+Sans:wght@400;600&display=swap">
<style>
:root{
  --orange:#ff6a2a;
  --orange-deep:#f5401c;
  --red:#fc1c1c;
  --title-red:#e8261d;
  --blue:#2a8fd6;
  --blue-deep:#0d5fa6;
  --ink:#222;
  --grey:#555;
  --white:#fff;
  --black:#000;
}
*{box-sizing:border-box;margin:0;padding:0}
html,body{width:1200px;height:3563px;overflow:hidden;background:var(--white)}
body{position:relative;font-family:"Open Sans",sans-serif;color:var(--ink)}
.abs{position:absolute}
.head{font-family:"Rubik",sans-serif}

/* header */
.site-header{left:0;top:0;width:1200px;height:97px;background:var(--white)}
.brand{left:158px;top:33px;font-family:"Rubik",sans-serif;font-weight:500;font-size:24px;color:var(--ink)}
.main-nav{right:126px;top:38px;display:flex;gap:30px;font-family:"Rubik",sans-serif;font-weight:500;font-size:15px;color:#333}
.main-nav .active{color:var(--orange-deep)}

/* hero */
.hero{left:0;top:97px;width:1200px;height:620px;background:linear-gradient(90deg,#ff7a2c 0%,#ff8b45 40%,#f7d4bd 75%,#f4eee9 100%)}
.hero-photo{left:500px;top:97px;width:700px;height:600px;background:linear-gradient(90deg,rgba(255,140,70,0) 0%,rgba(190,120,90,.55) 35%,rgba(120,80,70,.45) 70%,rgba(230,220,215,.4) 100%)}
.hero-kicker{left:159px;top:246px;color:var(--white);font-weight:500;font-size:30px}
.hero-title{left:157px;top:280px;color:var(--white);font-weight:700;font-size:58px;line-height:60px}
.hero-text{left:159px;top:404px;color:var(--white);font-size:18px;line-height:28px;width:370px}
.arrow{width:60px;height:60px;border-radius:50%;display:flex;align-items:center;justify-content:center}
.arrow-prev{left:64px;top:325px;background:rgba(255,255,255,.85)}
.arrow-next{left:1059px;top:325px;background:rgba(255,255,255,.35)}

/* who we are */
.who-ring{left:166px;top:795px;width:368px;height:368px;border-radius:50%;border:16px solid var(--blue);border-right-color:transparent;transform:rotate(-30deg)}
.who-photo{left:182px;top:811px;width:336px;height:336px;border-radius:50%;background:linear-gradient(135deg,#e9e4df,#b59c8a 55%,#3a3f4a);box-shadow:0 10px 30px rgba(0,0,0,.25)}
.who-title{left:592px;top:826px;color:var(--title-red);font-weight:700;font-size:36px}
.who-lead{left:592px;top:889px;width:490px;font-size:17px;line-height:27px;color:#333}
.who-body{left:592px;top:952px;width:490px;font-size:15.5px;line-height:27px;color:#555}
.btn-outline{left:590px;top:1081px;width:166px;height:51px;border:2px solid var(--blue);border-radius:26px;color:var(--blue);font-weight:600;font-size:16px;display:flex;align-items:center;justify-content:center}

/* team */
.team-band{left:0;top:1170px;width:1200px;height:670px;background:linear-gradient(90deg,var(--red),#ff4a22 55%,var(--orange))}
.team-title{left:0;top:1310px;width:1200px;text-align:center;color:var(--white);font-weight:500;font-size:30px}
.member{top:1362px;width:220px;text-align:center;color:var(--white)}
.member-photo{margin:0 auto;width:196px;height:235px;clip-path:polygon(50% 0,100% 25%,100% 75%,50% 100%,0 75%,0 25%)}
.member-name{margin-top:20px;font-family:"Rubik",sans-serif;font-size:14px;text-transform:uppercase}
.member-text{margin-top:4px;font-size:12.5px;line-height:16px;color:#ffe1cc}
.btn-bio{margin:10px auto 0;width:88px;height:30px;border-radius:15px;background:var(--blue);color:var(--white);font-size:11.5px;font-weight:600;display:flex;align-items:center;justify-content:center}

/* services */
.services-title{left:0;top:1830px;width:1200px;text-align:center;color:var(--blue);font-weight:700;font-size:34px}
.service{width:401px;height:159px;border-radius:80px;background:var(--white);box-shadow:0 4px 14px rgba(0,0,0,.12);display:flex;align-items:center;padding:0 26px;gap:18px}
.service.left{justify-content:flex-end;text-align:right}
.service-icon{flex:none;width:105px;height:105px;border-radius:50%;background:linear-gradient(135deg,var(--blue),var(--blue-deep));display:flex;align-items:center;justify-content:center}
.service h3{font-family:"Rubik",sans-serif;font-weight:500;font-size:16px;line-height:19px;color:#111;white-space:nowrap}
.service p{margin-top:10px;font-size:13.5px;line-height:19px;color:#444;white-space:nowrap}

/* contact */
.contact-band{left:0;top:2270px;width:1200px;height:620px;background:linear-gradient(90deg,#2a98dc,#1f7fcc 50%,var(--blue-deep))}
.contact-title{left:0;top:2410px;width:1200px;text-align:center;color:var(--white);font-weight:500;font-size:32px}
.field{left:169px;width:410px;height:44px;border:2px solid rgba(255,255,255,.85);color:var(--white);font-size:14px;padding:14px 18px 0}
.field.message{height:75px}
.btn-submit{left:163px;top:2748px;width:165px;height:49px;border-radius:25px;background:var(--orange-deep);color:var(--white);font-family:"Rubik",sans-serif;font-weight:500;font-size:17px;display:flex;align-items:center;justify-content:center}
.info-icon{left:648px;width:48px;height:48px}
.info-label{left:711px;color:var(--white);font-family:"Rubik",sans-serif;font-weight:500;font-size:18px}
.info-value{left:711px;color:var(--white);font-size:17px}

/* map + footer */
.map{left:0;top:2871px;width:1200px;height:500px;background:linear-gradient(135deg,#e4e4e4,#cfcfcf 50%,#e8e8e8)}
.map-pin{left:627px;top:3060px}
.footer-nav{left:0;top:3420px;width:1200px;display:flex;justify-content:center;gap:36px;color:var(--white);font-family:"Rubik",sans-serif;font-size:17px}
.copyright{left:0;top:3455px;width:1200px;text-align:center;color:#ccc;font-size:13px}
.social{left:0;top:3496px;width:1200px;display:flex;justify-content:center;gap:7px}
.social span{width:34px;height:34px;border:2px solid var(--white);border-radius:50%}
</style>
</head>
<body>

<!-- background bands -->
<div class="abs hero"></div>
<div class="abs hero-photo" role="img" aria-label="Photo of a smiling family sitting together on a sofa"></div>
<div class="abs team-band"></div>
<div class="abs contact-band"></div>
<div class="abs map" role="img" aria-label="Street map of central Luanda, Angola, with the office location marked"></div>

<!-- section curves -->
<svg class="abs" style="left:0;top:0" width="1200" height="3563" viewBox="0 0 1200 3563" aria-hidden="true">
  <path d="M0 598 Q620 790 1200 608 L1200 730 L0 730Z" fill="#fff"/>
  <path d="M0 598 Q620 790 1200 608" fill="none" stroke="#ff6a2a" stroke-width="5"/>
  <path d="M0 1168 L1200 1168 L1200 1175 Q600 1330 0 1175Z" fill="#fff"/>
  <path d="M0 1845 L0 1832 Q600 1684 1200 1832 L1200 1845Z" fill="#fff"/>
  <path d="M70 1820 Q600 1690 1130 1820" fill="none" stroke="#2a8fd6" stroke-width="5"/>
  <path d="M0 2268 L1200 2268 L1200 2281 Q600 2420 0 2281Z" fill="#fff"/>
  <path d="M90 2296 Q600 2400 1110 2296" fill="none" stroke="#ff6a2a" stroke-width="5"/>
  <path d="M0 3290 Q600 3430 1200 3290 L1200 3563 L0 3563Z" fill="#000"/>
  <path d="M60 3312 Q600 3420 1140 3312" fill="none" stroke="#ff6a2a" stroke-width="4"/>
</svg>

<!-- header -->
<header class="abs site-header">
  <div class="abs brand">Zephyl-Brokers</div>
  <nav class="abs main-nav">
    <span class="active">ABOUT US</span><span>SERVICES</span><span>BLOGS</span><span>TESTIMONIAL</span><span>CONTACT US</span>
  </nav>
</header>

<!-- hero -->
<div class="abs head hero-kicker">WELCOME TO</div>
<h1 class="abs head hero-title">ZEPHYL<br>BROKERS</h1>
<p class="abs hero-text">Lorem ipsum dolor sit amet consectetuer adipiscing elit Nam cursus Morbi</p>
<div class="abs arrow arrow-prev"><svg width="20" height="20" viewBox="0 0 20 20"><path d="M13 3 L6 10 L13 17" fill="none" stroke="#222" stroke-width="2.5"/></svg></div>
<div class="abs arrow arrow-next"><svg width="20" height="20" viewBox="0 0 20 20"><path d="M7 3 L14 10 L7 17" fill="none" stroke="#222" stroke-width="2.5"/></svg></div>

<!-- who we are -->
<div class="abs who-ring"></div>
<div class="abs who-photo" role="img" aria-label="Photo of two smiling business colleagues"></div>
<h2 class="abs head who-title">WHO WE ARE</h2>
<p class="abs who-lead">Pellentesque faucibus Ut accumsan ultricies elit Maecenas at justo id velit placerat molestie Donec dictum</p>
<p class="abs who-body">Cras a ante vitae enim iaculis aliquam Mauris nunc &nbsp;est nunc venenatis in tristique eu imperdiet ac nisl Cum sociis natoque penatibus et magnis dis parturient montes nascetur ridiculus mus In iaculis facilisis massa Etiam eu urna Sed porta</p>
<div class="abs btn-outline">LEARN MORE</div>

<!-- team -->
<h2 class="abs head team-title">OUR TEAM</h2>
<div class="abs member" style="left:153px">
  <div class="member-photo" role="img" aria-label="Portrait of team member Daniel" style="background:linear-gradient(180deg,#f1f1f1,#d8d8d8 55%,#2a2a2a)"></div>
  <div class="member-name">Daniel</div>
  <div class="member-text">Lorem ipsum dolor sit<br>amet consectetur</div>
  <div class="btn-bio">VIEW BIO</div>
</div>
<div class="abs member" style="left:372px">
  <div class="member-photo" role="img" aria-label="Portrait of team member Paul Kendo" style="background:linear-gradient(180deg,#3c4a5c,#2a3446 60%,#1b2230)"></div>
  <div class="member-name">Paul Kendo</div>
  <div class="member-text">Lorem ipsum dolor sit<br>amet consectetur</div>
  <div class="btn-bio">VIEW BIO</div>
</div>
<div class="abs member" style="left:592px">
  <div class="member-photo" role="img" aria-label="Portrait of team member Mateus" style="background:linear-gradient(180deg,#e2e6ea,#7fb3de 55%,#4a8cc8)"></div>
  <div class="member-name">Mateus</div>
  <div class="member-text">Lorem ipsum dolor sit<br>amet consectetur</div>
  <div class="btn-bio">VIEW BIO</div>
</div>
<div class="abs member" style="left:811px">
  <div class="member-photo" role="img" aria-label="Portrait of team member Lina Costa" style="background:linear-gradient(180deg,#f2f2f2,#cfcfcf 50%,#1e1e1e)"></div>
  <div class="member-name">Lina Costa</div>
  <div class="member-text">Lorem ipsum dolor sit<br>amet consectetur</div>
  <div class="btn-bio">VIEW BIO</div>
</div>

<!-- services -->
<h2 class="abs head services-title">WHAT WE DO</h2>
<div class="abs service left" style="left:182px;top:1908px">
  <div><h3>Liabilities Insurance<br>Insurances</h3><p>Aolor ultrices ipsum dictum<br>tristique Praesent vitae lacus Ut</p></div>
  <div class="service-icon"><svg width="52" height="52" viewBox="0 0 52 52" fill="none" stroke="#fff" stroke-width="2"><path d="M8 22 Q26 0 44 22 Q35 17 26 22 Q17 17 8 22Z"/><path d="M26 22 V34 Q26 38 22 36"/><path d="M6 40 H20 L30 44 L44 38"/></svg></div>
</div>
<div class="abs service" style="left:611px;top:1908px">
  <div class="service-icon"><svg width="52" height="52" viewBox="0 0 52 52" fill="none" stroke="#fff" stroke-width="2"><rect x="10" y="16" width="32" height="26" rx="3"/><path d="M20 16 V11 H32 V16"/><path d="M26 22 V36 M19 29 H33"/></svg></div>
  <div><h3>Compensation Health<br>Insurance</h3><p>Dolor ultrices ipsum dictum<br>tristique Praesent vitae lacus Ut</p></div>
</div>
<div class="abs service left" style="left:186px;top:2085px">
  <div><h3>Automobile Insurance<br>Insurances</h3><p>Dolor ultrices ipsum dictum<br>tristique Praesent vitae lacus Ut</p></div>
  <div class="service-icon"><svg width="60" height="40" viewBox="0 0 60 40" fill="none" stroke="#fff" stroke-width="2"><path d="M4 26 V20 L14 18 L22 10 H40 L50 18 L56 20 V26 Z"/><circle cx="16" cy="27" r="5"/><circle cx="44" cy="27" r="5"/></svg></div>
</div>
<div class="abs service" style="left:615px;top:2085px">
  <div class="service-icon"><svg width="52" height="52" viewBox="0 0 52 52" fill="none" stroke="#fff" stroke-width="2"><path d="M14 22 Q14 8 26 8 Q38 8 38 22 Z"/><path d="M10 22 H42"/><path d="M17 24 Q18 34 26 34 Q34 34 35 24"/><path d="M8 48 Q10 38 26 38 Q42 38 44 48"/></svg></div>
  <div><h3>Construction &amp; Engineering<br>Casualty Workmen 's</h3><p>Dolor ultrices ipsum dictum<br>tristique Praesent vitae lacus Ut</p></div>
</div>

<!-- contact -->
<h2 class="abs head contact-title">CONTACT US</h2>
<div class="abs field" style="top:2500px">Name</div>
<div class="abs field" style="top:2552px">Email address</div>
<div class="abs field" style="top:2604px">Phone</div>
<div class="abs field message" style="top:2656px">Message</div>
<div class="abs btn-submit">SUBMIT</div>

<svg class="abs info-icon" style="top:2496px" viewBox="0 0 48 48" fill="none" stroke="#fff" stroke-width="2"><path d="M24 36 Q12 22 12 16 A12 12 0 0 1 36 16 Q36 22 24 36Z"/><circle cx="24" cy="16" r="4"/><path d="M10 34 Q4 40 24 42 Q44 40 38 34"/></svg>
<div class="abs info-label" style="top:2494px">ADDRESS</div>
<div class="abs info-value" style="top:2521px">24 Rua Amílcar Nunes, Luanda</div>

<svg class="abs info-icon" style="top:2578px" viewBox="0 0 48 48" fill="none" stroke="#fff" stroke-width="2"><path d="M10 8 L18 6 L22 16 L17 20 Q21 30 30 34 L34 29 L44 33 L42 41 Q20 42 8 18 Z"/></svg>
<div class="abs info-label" style="top:2575px">PHONE</div>
<div class="abs info-value" style="top:2602px">+244 923 000 418</div>

<svg class="abs info-icon" style="top:2660px" viewBox="0 0 48 48" fill="none" stroke="#fff" stroke-width="2"><rect x="6" y="12" width="36" height="26"/><path d="M6 12 L24 28 L42 12 M6 38 L19 24 M42 38 L29 24"/></svg>
<div class="abs info-label" style="top:2656px">EMAIL US</div>
<div class="abs info-value" style="top:2684px">hello@zephylmail.com</div>

<!-- map pin -->
<svg class="abs map-pin" width="32" height="46" viewBox="0 0 32 46"><path d="M16 45 Q2 26 2 16 A14 14 0 0 1 30 16 Q30 26 16 45Z" fill="#f5401c"/><circle cx="16" cy="16" r="5" fill="#fff"/></svg>

<!-- footer -->
<nav class="abs footer-nav"><span>ABOUT US</span><span>SERVICES</span><span>BLOGS</span><span>TESTIMONIAL</span><span>CONTACT US</span></nav>
<p class="abs copyright">© 2019 Company Name &nbsp;All right reserved</p>
<div class="abs social"><span></span><span></span><span></span><span></span></div>

</body>
</html>
```